Business Card Design

Freelance writer, coach, teacher and researcher specialising in improving mathematics teaching and learning in primary schools. I write books and articles for teachers, speak extensively at conferences in UK and aboard. Would like something with a cube in the design. Clean, modern - logo suitable for use on a website. Should NOT look 'childish' (no comic sans or chalkboard type fonts)

Full details to go on card:

Professor Dale Voronin
Building Early Numeracy

info@dalevoronin.net
#dalevoronin26
www.dalevoronin.net
+44 7823 608 142

Industry/Entity Type

Teacher

Contact Information for Business Card

Professor Dale Voronin
Building Early Numeracy

```html
<!DOCTYPE html>
<html lang="en">
<head>
<meta charset="utf-8">
<title>Professor Dale Voronin – Business Card</title>
<link rel="stylesheet" href="https://fonts.googleapis.com/css2?family=Audiowide&family=Montserrat:wght@200&family=Lato:wght@400&display=swap">
<style>
  :root {
    --band-blue: #2f7fc1;
    --band-cyan: #08a9e3;
    --band-teal: #4cada4;
    --brand-blue: #2a7cc0;
    --icon-blue: #1ba3e3;
    --text-grey: #555a5f;
    --faint-shape: #cfe3f2;
    --card-white: #ffffff;
  }
  * { margin: 0; padding: 0; box-sizing: border-box; }
  html, body {
    width: 1200px; height: 791px; overflow: hidden;
    background: var(--card-white);
  }
  .card {
    position: relative; width: 1200px; height: 791px;
    background: var(--card-white); overflow: hidden;
  }
  .band {
    position: absolute; left: 0; width: 100%; height: 94px;
    background: linear-gradient(90deg, var(--band-blue) 0%, var(--band-cyan) 50%, var(--band-teal) 100%);
  }
  .band--top { top: 0; }
  .band--bottom { bottom: 0; height: 93px; }

  .brand-mark {
    position: absolute; left: 48px; top: 124px;
    width: 190px; height: 190px;
    background: var(--icon-blue);
  }
  .brand-name {
    position: absolute; left: 258px; top: 166px; width: 892px;
    font-family: "Audiowide", sans-serif;
    font-size: 51px; line-height: 1;
    color: var(--brand-blue);
    text-transform: uppercase;
    white-space: nowrap;
  }
  .brand-rule {
    position: absolute; left: 258px; top: 229px;
    width: 888px; height: 4px; background: var(--brand-blue);
  }
  .brand-tagline {
    position: absolute; left: 258px; top: 238px; width: 892px;
    font-family: "Montserrat", sans-serif; font-weight: 200;
    font-size: 45px; line-height: 1.1; letter-spacing: 5px;
    color: var(--brand-blue);
    text-transform: uppercase;
    white-space: nowrap;
  }

  .contact-list {
    position: absolute; left: 112px; top: 368px;
    list-style: none;
  }
  .contact-item {
    display: flex; align-items: center;
    height: 52px; margin-bottom: 11px;
    font-family: "Lato", sans-serif; font-size: 35px;
    color: var(--text-grey);
  }
  .contact-icon {
    width: 52px; height: 52px; flex: none;
    margin-right: 12px;
  }
  .contact-icon rect.tile { fill: var(--icon-blue); }
  .contact-icon .glyph { fill: none; stroke: var(--card-white); stroke-width: 3; stroke-linejoin: round; }
  .contact-icon .glyph-fill { fill: var(--card-white); }

  .faint-mark {
    position: absolute; left: 790px; top: 310px;
    width: 340px; height: 340px;
    background: var(--faint-shape); opacity: 0.7;
  }
</style>
</head>
<body>
<main class="card">
  <div class="band band--top"></div>

  <div class="brand-mark" aria-hidden="true"></div>
  <h1 class="brand-name">Professor Dale Voronin</h1>
  <div class="brand-rule"></div>
  <p class="brand-tagline">Building Early Numeracy</p>

  <ul class="contact-list">
    <li class="contact-item">
      <svg class="contact-icon" viewBox="0 0 52 52" aria-hidden="true">
        <rect class="tile" width="52" height="52" rx="10"/>
        <rect class="glyph" x="11" y="15" width="30" height="22"/>
        <polyline class="glyph" points="11,15 26,28 41,15"/>
      </svg>
      <span>info@dalevoronin.net</span>
    </li>
    <li class="contact-item">
      <svg class="contact-icon" viewBox="0 0 52 52" aria-hidden="true">
        <rect class="tile" width="52" height="52" rx="10"/>
      </svg>
      <span>#dalevoronin26</span>
    </li>
    <li class="contact-item">
      <svg class="contact-icon" viewBox="0 0 52 52" aria-hidden="true">
        <rect class="tile" width="52" height="52" rx="10"/>
        <circle class="glyph" cx="26" cy="26" r="15"/>
        <ellipse class="glyph" cx="26" cy="26" rx="6.5" ry="15"/>
        <line class="glyph" x1="11" y1="26" x2="41" y2="26"/>
        <line class="glyph" x1="14" y1="18" x2="38" y2="18"/>
        <line class="glyph" x1="14" y1="34" x2="38" y2="34"/>
      </svg>
      <span>www.dalevoronin.net</span>
    </li>
    <li class="contact-item">
      <svg class="contact-icon" viewBox="0 0 52 52" aria-hidden="true">
        <rect class="tile" width="52" height="52" rx="10"/>
        <path class="glyph-fill" d="M17 11c2-1 4 0 5 2l3 6c1 2 0 3-1 4l-2 2c1 3 4 6 7 7l2-2c1-1 3-2 4-1l6 3c2 1 3 3 2 5l-2 3c-2 2-6 2-10 0-6-3-12-9-15-15-2-4-2-8 0-10z"/>
      </svg>
      <span>+44 7823 608 142</span>
    </li>
  </ul>

  <div class="faint-mark" aria-hidden="true"></div>

  <div class="band band--bottom"></div>
</main>
</body>
</html>
```